User help guide for software for investment bank

We need a professional design for our user help guides for new software we have written for our client. We develop visualization software for investment banks in Singapore mainly focused in the financial and risk management area. Our help guides are design to show them how the software works as well as promote our brand
Updates

Project Deadline Extended Reason: I am looking for more alternative designs and we have around 10 more documents to do after this Added Saturday, November 21, 2015

Target Market(s)

Investment banking, risk management, finance

Industry/Entity Type

Bank

Requirements
Must have
• Content of document and logos
• Colour sheme
• Professional brouchure design
• Quorvin and bimsot logos on it
• Look at www.quorvin-example.com for company looks and feel
• PLEASE USE COLOUR SCHEMES BELOW IN ATTACHMENT AND FOLLOW SIMILAR STYLE TO CLIENT ANNUAL REPORT

```html
<!DOCTYPE html>
<html lang="en">
<head>
<meta charset="utf-8">
<title>Quorvin Web Editor Tool – User Guide</title>
<link rel="stylesheet" href="https://fonts.googleapis.com/css2?family=Arimo:wght@400;700&display=swap">
<style>
  :root {
    --backdrop: #ece8e3;
    --paper: #ffffff;
    --orange: #f7941d;
    --ink: #1f1f1f;
    --toc-ink: #4a4a4a;
    --table-head: #1ba6e8;
    --sky-top: #a9c6ea;
    --sky-bottom: #2f63b4;
    --rule: #222222;
  }
  * { box-sizing: border-box; margin: 0; padding: 0; }
  html, body { width: 1200px; height: 1000px; overflow: hidden; }
  body {
    background: var(--backdrop);
    font-family: "Arimo", Arial, sans-serif;
    color: var(--ink);
    position: relative;
  }
  .page {
    position: absolute;
    width: 540px;
    height: 770px;
    background: var(--paper);
    overflow: hidden;
    box-shadow: 0 6px 18px rgba(0,0,0,.18);
  }
  .page--cover { left: 45px; top: 115px; }
  .page--content { left: 615px; top: 95px; }

  /* Contents page */
  .contents-tab {
    position: absolute; left: 0; top: 62px;
    background: var(--orange);
    padding: 5px 26px 5px 32px;
    font-size: 21px; color: #3a3a3a;
  }
  .toc {
    position: absolute; left: 40px; top: 118px; width: 470px;
    list-style: none; color: var(--toc-ink);
  }
  .toc li {
    display: flex; font-size: 21px; line-height: 28px; white-space: nowrap;
  }
  .toc li .label { flex: none; }
  .toc li .dots { flex: 1; overflow: hidden; }
  .toc li .dots::after { content: "................................................................................"; }
  .toc li .num { flex: none; }
  .toc .sub { padding-left: 36px; }
  .toc .subsub { padding-left: 28px; }
  .toc .last { padding-left: 20px; }
  .cover-photo {
    position: absolute; left: 0; top: 400px; width: 100%; height: 370px;
    background: linear-gradient(160deg, var(--sky-top) 0%, #6d96d4 45%, var(--sky-bottom) 100%);
  }
  .corner {
    position: absolute; width: 90px; height: 90px;
  }
  .corner span {
    position: absolute; color: #fff; font-weight: 700; font-size: 20px;
  }
  .corner--left { left: 0; bottom: 0; }
  .corner--left span { left: 16px; bottom: 14px; }
  .corner--right { right: 0; bottom: 0; }
  .corner--right span { right: 16px; bottom: 14px; }

  /* Content page */
  .section-head {
    display: flex; align-items: center; gap: 8px;
    margin: 0 0 12px -40px;
  }
  .section-head h2 {
    background: var(--orange);
    font-size: 13px; font-weight: 700;
    padding: 6px 18px 6px 60px;
  }
  .section-head .plus { color: var(--orange); font-size: 24px; font-weight: 700; margin-top: -14px; }
  .content { position: absolute; left: 40px; top: 38px; right: 40px; font-size: 8.6px; line-height: 1.45; }
  .content p { margin-bottom: 8px; }
  .content h3 { font-size: 8.6px; font-weight: 700; margin: 12px 0 8px; }
  .roles { list-style: disc; padding-left: 32px; margin-bottom: 14px; }
  .roles ul { list-style: circle; padding-left: 22px; }
  .dash-list { list-style: none; padding-left: 22px; }
  .dash-list li::before { content: "-"; display: inline-block; width: 18px; margin-left: -18px; }
  .permissions {
    border-collapse: collapse; margin: 18px 0 26px 14px; width: 380px;
    font-size: 8px;
  }
  .permissions th {
    background: var(--table-head); color: #fff; font-weight: 700;
    text-align: left; padding: 3px 6px; vertical-align: top; line-height: 1.2;
  }
  .permissions td { border: 1px solid var(--rule); padding: 1px 6px; }
  .section-two { margin-top: 10px; }
</style>
</head>
<body>

<section class="page page--cover">
  <div class="contents-tab">Contents</div>
  <ol class="toc">
    <li><span class="label">1.&nbsp; User Roles and Permissions</span><span class="dots"></span><span class="num">3</span></li>
    <li><span class="label">2.&nbsp; Restrictions using Web Editor Tool</span><span class="dots"></span><span class="num">3</span></li>
    <li><span class="label">3.&nbsp; Navigation</span><span class="dots"></span><span class="num">4</span></li>
    <li class="sub"><span class="label">a.&nbsp; Data and Analytics pane</span><span class="dots"></span><span class="num">5</span></li>
    <li class="subsub"><span class="label">1.1.1&nbsp; Data Pane</span><span class="dots"></span><span class="num">5</span></li>
    <li class="subsub"><span class="label">1.1.2&nbsp; Analytics pane</span><span class="dots"></span><span class="num">6</span></li>
    <li class="sub"><span class="label">b.&nbsp; TOOLBAR</span><span class="dots"></span><span class="num">7</span></li>
    <li class="sub"><span class="label">c.&nbsp; Columns and Rows</span><span class="dots"></span><span class="num">8</span></li>
    <li class="sub"><span class="label">d.&nbsp; Marks</span><span class="dots"></span><span class="num">9</span></li>
    <li class="sub"><span class="label">e.&nbsp; FILTERS</span><span class="dots"></span><span class="num">9</span></li>
    <li class="last"><span class="label">4.&nbsp; Calculated Fields</span><span class="dots"></span><span class="num">9</span></li>
  </ol>
  <div class="cover-photo" role="img" aria-label="Photograph of a modern glass office tower rising against a clear blue sky"></div>
  <div class="corner corner--left">
    <svg width="90" height="90" viewBox="0 0 90 90"><polygon points="0,0 90,90 0,90" fill="var(--orange)"/></svg>
    <span>1</span>
  </div>
</section>

<section class="page page--content">
  <div class="content">
    <div class="section-head"><h2>1.&nbsp; User Roles and Permissions</h2><span class="plus">+</span></div>
    <p>The Web Editor Tool is allowed to be used to all the users that have <b>edit permissions</b> in their user role.</p>
    <p>Currently, RMVX tool has the roles below:</p>
    <ul class="roles">
      <li>Risk Administrator:
        <ul><li>Can do everything into Quorvin model.</li></ul></li>
      <li>Risk Project Leader
        <ul>
          <li>He can modify the report but NOT saving it or create a new one.</li>
          <li>He cannot move or delete the current reports stored at server</li>
          <li>He cannot set permissions</li>
        </ul></li>
      <li>Risk Publisher
        <ul><li>He can see the reports but do nothing more.</li></ul></li>
    </ul>

    <table class="permissions">
      <thead>
        <tr>
          <th>USER NAME</th>
          <th>Can access to Web Edit Tool</th>
          <th>Can modify the current report but no saving this</th>
          <th>Can create new reports or modify the current ones</th>
        </tr>
      </thead>
      <tbody>
        <tr><td>RISK ADMINISTRATOR</td><td>YES</td><td>N/A</td><td>YES</td></tr>
        <tr><td>RISK PROJECT LEADER</td><td>YES</td><td>YES</td><td>NO</td></tr>
        <tr><td>RISK PUBLISHER</td><td>NO</td><td>NO</td><td>NO</td></tr>
      </tbody>
    </table>

    <div class="section-head section-two"><h2>2.&nbsp; Restrictions using Web Editor Tool</h2><span class="plus">+</span></div>
    <p>Web Editor Tool contains big part of the current functionalities included at Quorvin Desktop. This allows to the users to modify or create new reports online, without using Quorvin Desktop. There are some rules that the users must bear in mind using the Web Editor Tool:</p>

    <h3>What the Web Editor Tool users can do:</h3>
    <ul class="dash-list">
      <li>Create new views (sheets), duplicate, and rename views in a workbook</li>
      <li>Change aggregation of measures</li>
      <li>Use <b>Show me</b> to create views</li>
      <li>View underlying data</li>
      <li>Create and edit <b>calculated fields</b>, and use quick table calculations</li>
      <li>Drag field to different mark types in the <b>Marks</b> card</li>
      <li>Use the Analytics pane to drag reference lines, trend lines, and other objects into the view</li>
      <li>Add, modify, and remove filters (Shown as <b>Quick Filters</b>), and edit a filter layout.</li>
      <li>Show labels, totals and subtotals</li>
      <li>Swap X and Y axes</li>
      <li>Change the view size</li>
      <li>Exclude or remove fields in the view</li>
    </ul>

    <h3>What the Web Editor Tool users cannot do:</h3>
    <ul class="dash-list">
      <li>Cannot add data sources to a published workbook</li>
      <li>Data model editing is not supported.</li>
      <li>Dashboards and stories cannot be created or modified at the server</li>
      <li>Formatting options are not available</li>
    </ul>
  </div>
  <div class="corner corner--right">
    <svg width="90" height="90" viewBox="0 0 90 90"><polygon points="90,0 90,90 0,90" fill="var(--orange)"/></svg>
    <span>2</span>
  </div>
</section>

</body>
</html>
```